Marketing Skill "Workouts"; Design for an e-mail attachment highlighting Marketing training subjects

I am a freelance marketing trainer based in Singapore and need to e-mail out an attachment (probably saved as a PDF) to potential clients showing the training services I offer. These clients are all large blue-chip multinational companies so the attachment needs to look professional/high quality when opened on a computer.

My Company is called "Brightline Marketing" (logo attached)

I am assuming the size should be A4 one sided colour.

I have attached some files that show best-attempts so far. These contain the key information, but the layouts all still look rather pedestrian. I am looking for something that looks a bit more dynamic but remains clear/easy to read.

Target Market(s)

HR/Marketing managers in multinational firms, mainly consumer goods

Industry/Entity Type

Marketing

Font styles to use
Sans Serif

Colors

Designer to choose colors to be used in the design.

Requirements
Must have
• Must look modern, up-to-date, professional.
Should not have
• Not gimmicky, like a cheap deal

```html
<!DOCTYPE html>
<html lang="en">
<head>
<meta charset="utf-8">
<title>Marketing Skill Workouts – Brightline Marketing</title>
<link rel="stylesheet" href="https://fonts.googleapis.com/css2?family=Oswald:wght@500;700&family=Lato:wght@300;400;700&family=Open+Sans:wght@400;600&display=swap">
<style>
  :root {
    --brand-red: #931a1e;
    --edge-grey: #9a9a9a;
    --tab-grey: #ececec;
    --ink: #1c1c1c;
    --ink-soft: #3a3a3a;
    --paper: #ffffff;
  }
  * { margin: 0; padding: 0; box-sizing: border-box; }
  html, body { width: 862px; height: 1200px; overflow: hidden; background: var(--paper); }
  .flyer { position: relative; width: 862px; height: 1200px; background: var(--paper); overflow: hidden; font-family: "Lato", Arial, sans-serif; }

  /* left column */
  .red-panel { position: absolute; left: 14px; top: 14px; width: 471px; height: 1171px; background: var(--brand-red); }
  .panel-edge { position: absolute; left: 485px; top: 14px; width: 7px; height: 1171px; background: var(--edge-grey); }
  .headline {
    position: absolute; left: 14px; top: 56px; width: 471px; text-align: center;
    font-family: "Oswald", "Arial Narrow", sans-serif; font-weight: 700;
    font-size: 86px; line-height: 84px; color: var(--paper); letter-spacing: -1px;
  }
  .hero { position: absolute; left: 14px; top: 330px; width: 478px; height: 338px; display: block; }

  .section-tab {
    position: absolute; left: 14px; width: 268px; height: 31px;
    background: var(--tab-grey);
    clip-path: polygon(0 0, 92% 0, 100% 50%, 92% 100%, 0 100%);
    font-family: "Open Sans", Arial, sans-serif; font-weight: 600;
    font-size: 21px; line-height: 31px; padding-left: 31px; color: var(--ink-soft);
  }
  .tab-topics { top: 688px; }
  .tab-benefits { top: 942px; }

  .check-list { position: absolute; left: 46px; list-style: none; font-family: "Open Sans", Arial, sans-serif; color: var(--paper); font-size: 14.5px; }
  .check-list li { position: relative; padding-left: 21px; white-space: nowrap; }
  .check-list li::before { content: "\2713"; position: absolute; left: 0; top: 0; font-size: 13px; }
  .topics-list { top: 727px; }
  .topics-list li { line-height: 21.6px; }
  .benefits-list { top: 983px; }
  .benefits-list li { line-height: 22.4px; }

  .website { position: absolute; left: 46px; top: 1115px; font-family: Arial, Helvetica, sans-serif; font-size: 36px; color: var(--paper); }

  /* right column */
  .right-col { position: absolute; left: 500px; width: 330px; text-align: center; }
  .hook { top: 64px; font-family: "Oswald", "Arial Narrow", sans-serif; font-weight: 700; font-size: 39px; line-height: 48px; color: var(--brand-red); }
  .hook-copy { top: 132px; font-weight: 300; font-size: 21px; line-height: 34.5px; color: var(--ink-soft); }

  .brand-name { position: absolute; left: 420px; top: 424px; width: 430px; text-align: center; font-family: "Lato", Arial, sans-serif; font-weight: 400; font-size: 34px; color: var(--ink); white-space: nowrap; }
  .brand-tagline { position: absolute; left: 420px; top: 474px; width: 430px; text-align: center; font-family: "Lato", Arial, sans-serif; font-weight: 700; font-size: 17px; color: var(--ink); }

  .promise { top: 592px; left: 480px; width: 370px; white-space: nowrap; font-weight: 300; font-size: 35px; line-height: 53px; color: var(--ink); }
  .why-title { top: 806px; font-family: "Open Sans", Arial, sans-serif; font-weight: 600; font-size: 27px; line-height: 36px; color: var(--brand-red); }
  .why-lead { top: 852px; font-size: 16px; line-height: 22px; color: var(--ink); }
  .why-body { top: 907px; font-size: 15.5px; line-height: 22px; color: var(--ink); }

  .contact-label { top: 1036px; font-family: Arial, Helvetica, sans-serif; font-size: 33px; line-height: 40px; color: var(--ink); }
  .contact-phone { top: 1078px; font-family: Arial, Helvetica, sans-serif; font-size: 38px; line-height: 46px; color: var(--brand-red); letter-spacing: 1px; }
  .contact-email { top: 1124px; left: 480px; width: 370px; font-family: Arial, Helvetica, sans-serif; font-size: 18px; line-height: 26px; color: var(--ink); letter-spacing: 1px; }
</style>
</head>
<body>
<main class="flyer">
  <div class="red-panel"></div>
  <div class="panel-edge"></div>

  <h1 class="headline">Marketing<br>Skill<br>“Workouts”</h1>

  <svg class="hero" viewBox="0 0 478 338" role="img" aria-label="Photograph of a muscular athlete lifting a dumbbell in a gym">
    <defs>
      <radialGradient id="gymTone" cx="45%" cy="45%" r="70%">
        <stop offset="0" stop-color="#c99a7c"/>
        <stop offset="0.5" stop-color="#8d6a58"/>
        <stop offset="1" stop-color="#3b2f2c"/>
      </radialGradient>
    </defs>
    <rect x="0" y="0" width="478" height="338" fill="url(#gymTone)"/>
    <circle cx="555" cy="170" r="185" fill="#ffffff" stroke="#9a9a9a" stroke-width="7"/>
  </svg>

  <div class="section-tab tab-topics">Key Topics:</div>
  <ul class="check-list topics-list">
    <li>Developing Strong Brand Plans</li>
    <li>Writing inspiring Briefs/Creative Evaluation</li>
    <li>Shopper Marketing/Developing Retail Promotions</li>
    <li>Brilliant Launch Management</li>
    <li>Improving Marketing R.O.I.</li>
    <li>Driving Brand Growth without Product Innovation</li>
    <li>Insight/Concept Development</li>
    <li>Integrating Digital Channels</li>
    <li>Creativity and Idea Generation</li>
  </ul>

  <div class="section-tab tab-benefits">Key Benefits:</div>
  <ul class="check-list benefits-list">
    <li>Latest in world-class thinking/tools/case studies</li>
    <li>Ability to “customize” to address your specific business issues</li>
    <li>Take-away “checklists” to embed behaviors and skills</li>
    <li>Asian context / relevance</li>
    <li>Proven quality</li>
  </ul>

  <div class="website">brightline-marketing.com</div>

  <h2 class="right-col hook">No time to learn?</h2>
  <p class="right-col hook-copy">Problem solved with 1 day<br>intensive workshops that will<br>drive business growth and<br>motivate your team</p>

  <div class="brand-name">Brightline Marketing</div>
  <div class="brand-tagline">Practical training that delivers</div>

  <p class="right-col promise">WORLD CLASS<br>QUALITY WITHOUT<br>THE COSTS</p>

  <h3 class="right-col why-title">Why me?</h3>
  <p class="right-col why-lead">The latest thinking, made<br>PRACTICAL and ACTIONABLE.</p>
  <p class="right-col why-body">20 years of business experience combined<br>with over 10 years of proven training /<br>facilitation for major “blue-chip” clients,<br>regularly scoring 90%+ satisfaction.</p>

  <div class="right-col contact-label">CONTACT</div>
  <div class="right-col contact-phone">+65 6555 0148</div>
  <div class="right-col contact-email">kenlowe@brightline-marketing.com</div>
</main>
</body>
</html>
```